Tallowmere Roofing Business Card

Need a business card with the logo that was designed here

Contact Information for Business Card

Name, Title, Phone, Email, Website, Company name

```html
<!DOCTYPE html>
<html lang="en">
<head>
<meta charset="utf-8">
<title>Tallowmere Roofing – Business Card</title>
<link rel="stylesheet" href="https://fonts.googleapis.com/css2?family=Montserrat:wght@400;500;700&display=swap">
<style>
  :root {
    --page-bg: #e9ebee;
    --brand-blue: #2878c2;
    --brand-dark: #2b3038;
    --ink: #3a3f47;
    --muted: #8d9096;
    --card-white: #ffffff;
  }
  * { box-sizing: border-box; margin: 0; padding: 0; }
  html, body {
    width: 1200px;
    height: 924px;
    overflow: hidden;
    background: var(--page-bg);
    font-family: "Montserrat", sans-serif;
  }
  .sheet {
    position: relative;
    width: 1200px;
    height: 924px;
  }
  .card {
    position: absolute;
    left: 250px;
    width: 700px;
    height: 400px;
    box-shadow: 0 10px 28px rgba(0,0,0,0.18);
  }
  .card--front {
    top: 40px;
    background: var(--brand-blue);
    display: flex;
    align-items: center;
    justify-content: center;
  }
  .card--back {
    top: 484px;
    background: var(--card-white);
  }
  .wordmark {
    display: flex;
    align-items: center;
    gap: 14px;
    font-weight: 700;
    letter-spacing: 0.02em;
    text-transform: uppercase;
    white-space: nowrap;
  }
  .wordmark__mark {
    width: 18px;
    height: 18px;
    flex: none;
  }
  .card--front .wordmark {
    font-size: 40px;
    color: var(--brand-dark);
  }
  .card--front .wordmark__mark { background: var(--brand-dark); width: 24px; height: 24px; }
  .card--back .wordmark {
    position: absolute;
    left: 44px;
    top: 238px;
    font-size: 22px;
    color: var(--brand-blue);
  }
  .card--back .wordmark__mark { background: var(--brand-blue); }
  .contact {
    position: absolute;
    left: 372px;
    top: 74px;
    color: var(--ink);
  }
  .contact__name {
    font-size: 30px;
    font-weight: 700;
    color: var(--brand-blue);
    letter-spacing: 0.01em;
    text-transform: uppercase;
    line-height: 1.1;
  }
  .contact__title {
    font-size: 19px;
    font-weight: 400;
    color: var(--muted);
    margin-top: 4px;
    margin-bottom: 18px;
  }
  .contact__list { list-style: none; }
  .contact__item {
    display: flex;
    align-items: flex-start;
    gap: 12px;
    font-size: 15px;
    line-height: 1.45;
    margin-bottom: 6px;
  }
  .contact__icon {
    width: 14px;
    height: 14px;
    margin-top: 4px;
    flex: none;
    fill: var(--brand-blue);
  }
</style>
</head>
<body>
<main class="sheet">
  <section class="card card--front" aria-label="Card front">
    <div class="wordmark">
      <span class="wordmark__mark"></span>
      <span>Tallowmere Roofing</span>
    </div>
  </section>

  <section class="card card--back" aria-label="Card back">
    <div class="wordmark">
      <span class="wordmark__mark"></span>
      <span>Tallowmere Roofing</span>
    </div>

    <div class="contact">
      <h1 class="contact__name">Daniel Hartley</h1>
      <p class="contact__title">Founder &amp; CEO</p>
      <ul class="contact__list">
        <li class="contact__item">
          <svg class="contact__icon" viewBox="0 0 14 14" aria-hidden="true"><path d="M7 0a5 5 0 0 0-5 5c0 3.6 5 9 5 9s5-5.4 5-9a5 5 0 0 0-5-5zm0 7a2 2 0 1 1 0-4 2 2 0 0 1 0 4z"/></svg>
          <span>48 Birchwood Lane<br>Millbrook, NY 12545</span>
        </li>
        <li class="contact__item">
          <svg class="contact__icon" viewBox="0 0 14 14" aria-hidden="true"><path d="M3 0l2.5 3-1.5 2c.8 1.8 2.2 3.2 4 4l2-1.5 3 2.5-1.5 2.5C6 12.5 1.5 8 1 1.5z"/></svg>
          <span>(555) 214-3098</span>
        </li>
        <li class="contact__item">
          <svg class="contact__icon" viewBox="0 0 14 14" aria-hidden="true"><path d="M0 3h14v8H0zm1 .8v.4l6 3.6 6-3.6v-.4z"/></svg>
          <span>hello@tallowmereroofing.com</span>
        </li>
        <li class="contact__item">
          <svg class="contact__icon" viewBox="0 0 14 14" aria-hidden="true"><path d="M7 0a7 7 0 1 0 0 14A7 7 0 0 0 7 0zm0 1.5c.9 1.2 1.5 3 1.6 4.8H5.4C5.5 4.5 6.1 2.7 7 1.5zM5.4 7.7h3.2c-.1 1.8-.7 3.6-1.6 4.8-.9-1.2-1.5-3-1.6-4.8z"/></svg>
          <span>www.tallowmereroofing.com</span>
        </li>
      </ul>
    </div>
  </section>
</main>
</body>
</html>
```